Hochzeitseinladung
Zielgruppe
Gastronomie - Zielgruppe ist ein Hochzeitspaar, welches bei uns feiert. Wir dürfen Ihre Hochzeitseinladung entwerfen.
Aufgabenstellung
Den Textvorschlag des Brautpaares findet Ihr im Anhang. Das Thema der Hochzeit ist AMORE.
1. Die Hochzeitseinladung darf gerne kreativ gestaltet sein, vielleicht in Form des Moodboard-Bildes im Anhang? Mattes hat braune Haare und Locken und Doreen lange braune Haare. Beide tragen eine Brille.
Das Hochzeitspaar hat noch einen kleinen braunen Zwergpudel 'Fips', vielleicht findet er auch noch Platz auf der Einladungskarte ;-).
2. Als Alternativ-Vorschlag wäre ein klassisches Design auf zB geprägtem Papier toll.
3. Etwas Schlichtes mit einem Neon-Accessoire würde das Hochzeitspaar auch gut finden. Zb brauner Karton mit einem Neonband.

```html
<!DOCTYPE html>
<html lang="de">
<head>
<meta charset="utf-8">
<title>Hochzeitseinladung Doreen &amp; Mattes</title>
<link rel="stylesheet" href="https://fonts.googleapis.com/css2?family=Cormorant+Garamond:wght@400;500;600&family=Montserrat:wght@300;400;500;600&family=Playfair+Display:wght@400&family=Mrs+Saint+Delafield&display=swap">
<style>
  :root {
    --backdrop: #e7e6e3;
    --paper: #ffffff;
    --gold: #d4b673;
    --ink: #6e6e6a;
    --ink-dark: #2f2f2f;
    --placeholder: #ecebe8;
  }
  * { margin: 0; padding: 0; box-sizing: border-box; }
  html, body { width: 1200px; height: 873px; overflow: hidden; }
  body { background: var(--backdrop); position: relative; font-family: "Cormorant Garamond", serif; }

  .card {
    position: absolute;
    background: var(--paper);
    box-shadow: 0 10px 24px rgba(0,0,0,0.12);
  }

  /* Front card */
  .card--front { left: 130px; top: 215px; width: 430px; height: 590px; }
  .theme-lettering {
    position: absolute; left: 28px; top: 30px; width: 78px; height: 38px;
    background: var(--placeholder); border-radius: 4px;
  }
  .monogram {
    position: absolute; left: 0; right: 0; top: 150px; height: 180px;
    display: flex; justify-content: center; align-items: flex-end; gap: 6px;
    color: var(--gold); font-family: "Playfair Display", serif; line-height: 1;
  }
  .monogram__letter { font-size: 150px; font-weight: 400; }
  .monogram__letter--second { margin-bottom: 40px; }
  .monogram__tagline {
    writing-mode: vertical-rl; transform: rotate(180deg);
    font-family: "Cormorant Garamond", serif; font-size: 11px; letter-spacing: 4px;
    margin-bottom: 14px; margin-right: 4px;
  }
  .front-names {
    position: absolute; left: 0; right: 0; top: 410px; text-align: center;
    font-family: "Montserrat", sans-serif; font-weight: 400; font-size: 18px;
    letter-spacing: 5px; color: var(--gold);
  }
  .front-date {
    position: absolute; left: 0; right: 0; top: 455px; text-align: center;
    font-family: "Montserrat", sans-serif; font-weight: 600; font-size: 17px;
    letter-spacing: 2px; color: var(--gold);
  }
  .front-date span { font-weight: 300; margin: 0 6px; }
  .front-place {
    position: absolute; left: 0; right: 0; top: 505px; text-align: center;
    font-family: "Montserrat", sans-serif; font-weight: 300; font-size: 13px;
    letter-spacing: 3px; color: var(--gold);
  }

  /* Details card */
  .card--details { left: 700px; top: 28px; width: 430px; height: 600px; text-align: center; }
  .script-title {
    font-family: "Mrs Saint Delafield", cursive; color: var(--gold); font-weight: 400; line-height: 1;
  }
  .details-title { position: absolute; left: 0; right: 0; top: 70px; font-size: 92px; }
  .details-subtitle {
    position: absolute; left: 0; right: 0; top: 172px;
    font-size: 11px; letter-spacing: 0.8px; color: var(--ink); text-transform: uppercase;
  }
  .timeline { position: absolute; left: 25px; top: 218px; width: 380px; height: 160px; }
  .timeline__icon {
    position: absolute; top: 0; width: 42px; height: 42px; margin-left: -21px;
    background: var(--placeholder); border-radius: 50%;
  }
  .timeline__track { position: absolute; left: 0; top: 48px; }
  .timeline__stop {
    position: absolute; top: 64px; width: 84px; margin-left: -42px;
    color: var(--ink); line-height: 1.15;
  }
  .timeline__time { font-size: 12px; font-weight: 600; display: block; margin-bottom: 2px; white-space: nowrap; }
  .timeline__label { font-size: 8px; letter-spacing: 0.4px; text-transform: uppercase; display: block; }
  .section-title { position: absolute; left: 0; right: 0; font-size: 32px; }
  .section-title--registry { top: 388px; }
  .section-title--dress { top: 500px; }
  .section-text {
    position: absolute; left: 36px; right: 36px; font-size: 12px; line-height: 1.3; color: var(--ink);
  }
  .section-text--registry { top: 420px; }
  .section-text--dress { top: 534px; }
</style>
</head>
<body>

<section class="card card--front" aria-label="Einladungskarte Vorderseite">
  <div class="theme-lettering" role="img" aria-label="Handgeschriebener Schriftzug Amore mit kleinem Herz"></div>
  <div class="monogram">
    <span class="monogram__letter">D</span>
    <span class="monogram__tagline">WE SAY YES</span>
    <span class="monogram__letter monogram__letter--second">M</span>
  </div>
  <p class="front-names">DOREEN &amp; MATTES</p>
  <p class="front-date">20<span>|</span>04<span>|</span>24</p>
  <p class="front-place">Münster</p>
</section>

<section class="card card--details" aria-label="Einladungskarte Details">
  <h1 class="script-title details-title">Details</h1>
  <p class="details-subtitle">Zeitplan für unsere Hochzeit</p>

  <div class="timeline">
    <div class="timeline__icon" style="left:45px" role="img" aria-label="Symbol Kirche"></div>
    <div class="timeline__icon" style="left:142px" role="img" aria-label="Symbol anstoßende Sektgläser"></div>
    <div class="timeline__icon" style="left:238px" role="img" aria-label="Symbol Uhr und Kaffeetasse"></div>
    <div class="timeline__icon" style="left:335px" role="img" aria-label="Symbol Teller mit Besteck"></div>
    <svg class="timeline__track" width="380" height="14" viewBox="0 0 380 14" aria-hidden="true">
      <line x1="45" y1="7" x2="335" y2="7" stroke="#2f2f2f" stroke-width="1"/>
      <circle cx="45" cy="7" r="4" fill="#2f2f2f"/>
      <circle cx="142" cy="7" r="4" fill="#2f2f2f"/>
      <circle cx="238" cy="7" r="4" fill="#2f2f2f"/>
      <circle cx="335" cy="7" r="4" fill="#2f2f2f"/>
    </svg>
    <div class="timeline__stop" style="left:45px">
      <span class="timeline__time">13:30 Uhr</span>
      <span class="timeline__label">Standesamt Kloster am Lindenhof</span>
    </div>
    <div class="timeline__stop" style="left:142px">
      <span class="timeline__time">14:30 UHR</span>
      <span class="timeline__label">Sektempfang Salon Abendrot</span>
    </div>
    <div class="timeline__stop" style="left:238px">
      <span class="timeline__time">AB 16:00 UHR</span>
      <span class="timeline__label">Kurze Pause</span>
    </div>
    <div class="timeline__stop" style="left:335px">
      <span class="timeline__time">18:30UHR</span>
      <span class="timeline__label">Einfinden im Gasthaus Alter Fuhrmann</span>
    </div>
  </div>

  <h2 class="script-title section-title section-title--registry">Standesamt</h2>
  <p class="section-text section-text--registry">Im Standesamt stehen leider nur 20 Plätze zur Verfügung. Falls Ihr Interesse habt, freue ich mich über Eure Nachricht, damit wir gemeinsam eine Lösung finden können.</p>

  <h2 class="script-title section-title section-title--dress">Dresscodes</h2>
  <p class="section-text section-text--dress">Tagsüber : Cocktail<br>Abends: Festlich elegant &amp; dunkler Anzug</p>
</section>

</body>
</html>
```